International Comedian HARRIET MOSS Needs A New Show Poster

Multi-award winning Harriet Moss is one of Australia's most exciting comic performers. Since her stand up comedy debut in 2008, she has rapidly gained an international reputation as a remarkable live comic.
BIO:
http://plorvane.com/cms-plorvane-artists/harriet-moss.php
We are looking to take the images attached (one copy on black background and a reverse on white background), incorporate the title of the show and base a design around the title and theme of the show, though this is also not essential if you have a good idea that looks cool based on the image but having nothing to do with the title.
The Title of the show is:
THE LANTERN
This must be included on the poster somewhere
The show is about:
This has nothing to do with Anselmo Trevisani. And it ain’t about lettuce. It’s about perspective- what we see, what we think we know, and what is actually going on. You know what’s underneath the tip of THE LANTERN? The rest of THE LANTERN.
For all the moments where you think you understand the enormity of a situation, then the water drains; and you step back to realise what you’re really dealing with.
Notes from inital draft:
"I was thinking about your idea of having an iceberg in the back. I can't remember if you suggested it, but what about the idea of a single black pen outline of an iceberg (illustrated) behind me and then real iceberg chunks and water around my knees/feet? "
- Must have a space down the bottom that touring information can be added. whether this is overlay-ed or in a box is up to you.
- be clean and simple,
- draw the eye
- have a eye catching color scheme

```html
<!DOCTYPE html>
<html lang="en">
<head>
<meta charset="utf-8">
<title>The Lantern – Harriet Moss</title>
<link href="https://fonts.googleapis.com/css2?family=Open+Sans:wght@400;600;700;800&display=swap" rel="stylesheet">
<style>
  :root {
    --page: #e3e9f0;
    --navy-deep: #070b33;
    --navy: #0d1447;
    --sea: #1b2e6e;
    --sky-pale: #cfd2d8;
    --sky-mid: #8f9fb8;
    --ice-white: #eef3f8;
    --ice-blue: #8fb2cf;
    --ice-shadow: #4f6f93;
    --title-pale: #d9dde3;
    --skin-pink: #e6b6bd;
    --veil-white: #f2f2f4;
    --text-white: #ffffff;
    --rule: #9aa2c0;
  }
  * { margin: 0; padding: 0; box-sizing: border-box; }
  html, body {
    width: 1093px; height: 1200px; overflow: hidden;
    background: var(--page);
    font-family: "Open Sans", Arial, sans-serif;
  }
  .poster {
    position: absolute; left: 106px; top: 31px;
    width: 880px; height: 1137px; overflow: hidden;
    background: var(--navy-deep);
  }
  .scene-backdrop {
    position: absolute; left: 0; top: 0; width: 880px; height: 760px;
    background: linear-gradient(180deg, var(--sky-pale) 0%, #bfc5cf 28%, var(--sky-mid) 40%, var(--sea) 52%, var(--navy-deep) 100%);
  }
  .iceberg-photo {
    position: absolute; left: 76px; top: 90px; width: 690px; height: 860px;
    border-radius: 46% 46% 30% 30% / 22% 22% 12% 12%;
    background: radial-gradient(ellipse at 50% 20%, var(--ice-white) 0%, var(--ice-blue) 30%, var(--ice-shadow) 55%, rgba(7,11,51,0) 78%);
    opacity: .85;
  }
  .performer-photo {
    position: absolute; left: 41px; top: 456px; width: 543px; height: 495px;
    border-radius: 40% 40% 20% 20%;
    background: radial-gradient(ellipse at 50% 55%, var(--skin-pink) 0%, var(--veil-white) 38%, rgba(242,242,244,0.25) 62%, rgba(7,11,51,0) 75%);
  }
  .show-title {
    position: absolute; font-weight: 700; line-height: 1; letter-spacing: 1px;
  }
  .show-title--top {
    left: 337px; top: 258px; font-size: 82px; color: var(--navy);
  }
  .show-title--mirrored {
    right: 69px; top: 340px; font-size: 116px; color: var(--title-pale);
    transform: scaleY(-1); transform-origin: center;
  }
  .tagline {
    position: absolute; left: 588px; top: 446px;
    color: var(--text-white); font-weight: 700; font-size: 35px; line-height: 45px;
  }
  .performer-name {
    position: absolute; right: 28px; top: 962px;
    color: var(--text-white); font-weight: 700; font-size: 46px; line-height: 1;
  }
  .tour-dates {
    position: absolute; top: 1031px; color: var(--text-white);
    text-align: right; font-size: 15.5px; line-height: 20px;
  }
  .tour-dates__venue { font-weight: 700; font-size: 19px; line-height: 25px; }
  .tour-dates--canberra { right: 578px; }
  .tour-dates--london { right: 28px; }
  .tour-divider {
    position: absolute; left: 400px; top: 1034px; width: 1px; height: 73px;
    background: var(--rule);
  }
</style>
</head>
<body>
  <main class="poster">
    <div class="scene-backdrop" role="img" aria-label="Grey sky over a deep blue sea"></div>
    <div class="iceberg-photo" role="img" aria-label="Photograph of an iceberg above and below the waterline, a faint eye blended into the ice"></div>
    <div class="performer-photo" role="img" aria-label="Photograph of the performer seated in a pink dress and white shawl with a white cockatoo on her arm"></div>

    <h1 class="show-title show-title--top">THE LAN</h1>
    <div class="show-title show-title--mirrored" aria-hidden="true">TERN</div>

    <p class="tagline">Do you<br>know what’s<br>underneath?</p>

    <h2 class="performer-name">HARRIET MOSS</h2>

    <div class="tour-dates tour-dates--canberra">
      <div class="tour-dates__venue">DUSKFAIR | CANBERRA</div>
      <div>25th - 27th September</div>
      <div>Tickets via DuskFair</div>
    </div>
    <div class="tour-divider"></div>
    <div class="tour-dates tour-dates--london">
      <div class="tour-dates__venue">JESTER HALL | LONDON</div>
      <div>13th September | More information via Jester Hall</div>
      <div>14st Septmber | More information via Jester Hall</div>
    </div>
  </main>
</body>
</html>
```